Small Accounting Practice needs something creative

We need a business card design for a new small accounting practice based in Perth, Australia. The name of the practice is 'Kowra Ledger Partners Pty Ltd'. We providing Tax, Bookkeeping and Accounting services. Our target are individuals and small businesses. We want the design to be simply and creative. Also, we can the design can help us to gain people's trust.

Target Market(s)

Individuals and small businesses.

Industry/Entity Type

Accounting

Colors

Designer to choose colors to be used in the design.

```html
<!DOCTYPE html>
<html lang="en">
<head>
<meta charset="utf-8">
<title>Kowra Ledger Partners – Business Card</title>
<link href="https://fonts.googleapis.com/css2?family=Open+Sans:ital,wght@0,400;0,700;1,400;1,700&display=swap" rel="stylesheet">
<style>
  :root{
    --bg:#e9ecef;
    --card:#ffffff;
    --blue:#0a86b3;
    --gold:#f6b312;
    --white:#ffffff;
  }
  html,body{margin:0;padding:0;width:1200px;height:901px;overflow:hidden;background:var(--bg);font-family:"Open Sans",Arial,sans-serif;}
  .stage{position:relative;width:1200px;height:901px;}
  .card{position:absolute;left:290px;width:620px;height:354px;border-radius:26px;background:var(--card);overflow:hidden;box-shadow:0 10px 28px rgba(0,0,0,.18);}
  .card--front{top:56px;}
  .card--back{top:490px;}
  .card__art{position:absolute;inset:0;width:620px;height:354px;}
  .brand{position:absolute;display:flex;align-items:center;gap:14px;color:var(--blue);font-weight:700;font-style:italic;}
  .brand__dot{width:50px;height:50px;border-radius:50%;background:var(--blue);flex:none;}
  .card--front .brand{left:40px;top:24px;font-size:30px;line-height:1.08;}
  .card--back .brand{left:350px;top:60px;font-size:27px;line-height:1.08;}
  .person{position:absolute;left:34px;top:258px;color:var(--white);font-style:italic;}
  .person__name{font-size:22px;font-weight:700;margin:0;}
  .person__role{font-size:15px;margin:2px 0 0;}
  .contacts{position:absolute;right:30px;top:220px;margin:0;padding:0;list-style:none;color:var(--white);font-style:italic;font-size:12.5px;text-align:right;line-height:1.55;}
  .contacts li{display:flex;justify-content:flex-end;align-items:center;gap:7px;}
  .contacts svg{width:11px;height:11px;flex:none;}
  .website{position:absolute;left:40px;top:272px;color:var(--white);font-style:italic;font-size:14px;letter-spacing:4px;}
</style>
</head>
<body>
<div class="stage">

  <section class="card card--front" aria-label="Card front">
    <svg class="card__art" viewBox="0 0 620 354" aria-hidden="true">
      <path d="M0,156 C200,148 420,162 620,202 L620,354 L0,354 Z" fill="var(--blue)"/>
      <path d="M0,124 C200,116 420,130 620,166 L620,175 C420,139 200,125 0,133 Z" fill="var(--gold)"/>
      <path d="M0,140 C200,132 420,146 620,184 L620,192 C420,154 200,140 0,148 Z" fill="var(--gold)"/>
    </svg>
    <div class="brand"><span class="brand__dot"></span><span>Kowra Ledger<br>Partners</span></div>
    <div class="person">
      <p class="person__name">Dara Whitcombe</p>
      <p class="person__role">Owner / CEO</p>
    </div>
    <ul class="contacts">
      <li>Level 3, 14 Hay St, Perth WA 6000<svg viewBox="0 0 12 12"><path d="M6 1a3.5 3.5 0 0 0-3.5 3.5C2.5 7.5 6 11 6 11s3.5-3.5 3.5-6.5A3.5 3.5 0 0 0 6 1zm0 5a1.4 1.4 0 1 1 0-2.8A1.4 1.4 0 0 1 6 6z" fill="var(--white)"/></svg></li>
      <li>08-9321-4470<svg viewBox="0 0 12 12"><path d="M3 1l2 2.5-1 1.2a6 6 0 0 0 3.3 3.3l1.2-1L11 9l-1.2 1.8C5.5 10.5 1.5 6.5 1.2 2.2z" fill="var(--white)"/></svg></li>
      <li>0412-558-903<svg viewBox="0 0 12 12"><rect x="3.5" y="1" width="5" height="10" rx="1" fill="var(--white)"/></svg></li>
      <li>08-9321-4471<svg viewBox="0 0 12 12"><rect x="1.5" y="3" width="9" height="6" rx="1" fill="var(--white)"/></svg></li>
      <li>hello@kowraledger.au<svg viewBox="0 0 12 12"><rect x="1" y="2.5" width="10" height="7" rx="1" fill="var(--white)"/><path d="M1.5 3l4.5 3.5L10.5 3" stroke="var(--blue)" fill="none"/></svg></li>
      <li>www.kowraledger.au<svg viewBox="0 0 12 12"><circle cx="6" cy="6" r="5" fill="var(--white)"/></svg></li>
    </ul>
  </section>

  <section class="card card--back" aria-label="Card back">
    <svg class="card__art" viewBox="0 0 620 354" aria-hidden="true">
      <path d="M0,0 L150,0 C215,130 370,262 620,312 L620,354 L0,354 Z" fill="var(--blue)"/>
      <path d="M166,0 L178,0 C240,120 390,246 620,290 L620,298 C380,256 225,130 166,0 Z" fill="var(--gold)"/>
      <path d="M190,0 L204,0 C260,110 400,228 620,268 L620,280 C392,240 245,120 190,0 Z" fill="var(--gold)"/>
    </svg>
    <div class="brand"><span class="brand__dot"></span><span>Kowra Ledger<br>Partners</span></div>
    <div class="website">www.kowraledger.au</div>
  </section>

</div>
</body>
</html>
```